Website update for Harborline Ledger & Payroll Services

Our website needs updating
www.harborlineledgerservices.com
Here are some of our latest print pieces to use as a guide?
I have also attached our graphic identity guide which includes the Pantone colors

Target Market(s)

Insurance Agencies

Industry/Entity Type

Accounting

Number of Pages Required

5+ page

```html
<!DOCTYPE html>
<html lang="en">
<head>
<meta charset="utf-8">
<title>Harborline Ledger &amp; Payroll Services</title>
<link href="https://fonts.googleapis.com/css2?family=Raleway:wght@300;400;500;600&family=Open+Sans:wght@400;600&display=swap" rel="stylesheet">
<style>
:root{
  --teal:#19ab9b;
  --teal-dark:#148a7e;
  --teal-deep:#0f6f66;
  --aqua:#8eefe8;
  --ink:#3d3d3d;
  --grey:#6f6f6f;
  --white:#ffffff;
  --hero-a:#f3f5f6;
  --hero-b:#d9dfe2;
}
*{box-sizing:border-box;margin:0;padding:0}
html,body{width:1200px;height:3680px;overflow:hidden}
body{font-family:"Open Sans",Arial,sans-serif;color:var(--ink);background:var(--white);position:relative}

.site-nav{position:absolute;top:0;left:0;width:1200px;height:48px;display:flex;justify-content:center;gap:46px;align-items:center;z-index:2}
.site-nav a{font-family:"Raleway",sans-serif;font-size:15px;color:var(--grey);text-decoration:none;padding:12px 0;border-bottom:3px solid transparent}
.site-nav a.active{color:var(--teal);border-bottom-color:var(--teal)}

.hero{position:absolute;top:0;left:0;width:1200px;height:660px}
.hero-photo{position:absolute;inset:0;background:linear-gradient(120deg,var(--hero-a) 0%,var(--white) 45%,var(--hero-b) 100%)}
.hero-brand{position:absolute;top:210px;left:300px;width:600px;display:flex;align-items:center;gap:22px;justify-content:center}
.hero-brand .mark{width:70px;height:70px;background:var(--teal);flex:none}
.hero-brand span{font-family:"Raleway",sans-serif;font-weight:600;font-size:40px;line-height:1.15;color:var(--ink)}
.hero-dots{position:absolute;bottom:24px;left:0;width:100%;display:flex;justify-content:center;gap:14px}
.hero-dots i{width:10px;height:10px;border-radius:50%;background:#c9d0d3;display:block}
.hero-dots i.on{background:var(--teal)}

.about{position:absolute;top:660px;left:0;width:1200px;height:300px;background:var(--teal);color:var(--white);text-align:center;padding-top:40px}
.about h2{font-family:"Raleway",sans-serif;font-weight:400;font-size:44px}
.about p{width:760px;margin:26px auto 0;font-size:14px;line-height:1.7}
.btn-outline{display:inline-block;margin-top:26px;padding:8px 26px;border:2px solid var(--white);border-radius:20px;font-size:15px;color:var(--white);text-decoration:none}

.service{position:absolute;left:0;width:1200px;height:310px;display:flex;align-items:center}
.service.tint{background:var(--aqua)}
.service .art{width:400px;height:240px;border-radius:6px;flex:none}
.service .copy{width:460px}
.service h3{font-family:"Raleway",sans-serif;font-weight:400;font-size:33px;line-height:1.2;color:var(--teal);text-transform:uppercase}
.service.tint h3{color:var(--teal-deep)}
.service p{margin-top:14px;font-size:14px;line-height:1.65;color:var(--grey)}
.service.tint p{color:var(--ink)}
.service.art-left .art{margin-left:160px;margin-right:40px}
.service.art-right .copy{margin-left:80px}
.service.art-right .art{margin-left:180px}

.why{position:absolute;top:3130px;left:0;width:1200px;height:340px;background:var(--teal);color:var(--white);text-align:center;padding-top:30px}
.why h2{font-family:"Raleway",sans-serif;font-weight:400;font-size:44px}
.why-list{display:flex;justify-content:center;gap:80px;margin-top:40px}
.why-item{width:200px}
.why-item svg{width:110px;height:110px}
.why-item span{display:block;margin-top:18px;font-size:17px}

.site-footer{position:absolute;top:3470px;left:0;width:1200px;height:210px;background:var(--teal-dark);color:var(--white)}
.footer-bar{display:flex;align-items:center;justify-content:space-between;padding:24px 80px 0}
.footer-links{display:flex;gap:42px;font-size:14px;font-weight:600}
.footer-links a{color:var(--white);text-decoration:none}
.footer-links a.pill{border:2px solid var(--white);border-radius:16px;padding:4px 16px}
.social{display:flex;gap:14px}
.social i{width:34px;height:34px;border-radius:50%;border:2px solid var(--white);display:block}
.contact{display:flex;gap:120px;padding:36px 80px 0;font-size:14px;align-items:center}
.contact div{display:flex;align-items:center;gap:12px}
.contact svg{width:22px;height:22px}
.copyright{position:absolute;bottom:0;left:0;width:100%;height:56px;background:var(--teal-deep);display:flex;align-items:center;justify-content:center;font-size:13px}
</style>
</head>
<body>

<header class="hero">
  <div class="hero-photo" role="img" aria-label="Photo of a hand pressing keys on a desk calculator"></div>
  <nav class="site-nav">
    <a href="#">Home</a><a class="active" href="#">About Us</a><a href="#">Company</a><a href="#">Our Services</a><a href="#">How it Works</a><a href="#">Resources</a><a href="#">Contact Us</a><a href="#">Blog</a>
  </nav>
  <div class="hero-brand"><div class="mark"></div><span>Harborline Ledger &amp; Payroll Services</span></div>
  <div class="hero-dots"><i class="on"></i><i></i><i></i></div>
</header>

<section class="about">
  <h2>About Us</h2>
  <p>Welcome to Harborline. After years of running in-house accounting for agencies, Dana Whitcombe founded the firm in 2011 to help independent insurance agencies manage their accounting and bookkeeping. Our trained staff work in our Connecticut office across every part of agency management systems, and we have room to take on new members. Call us to meet your unique needs.</p>
  <a class="btn-outline" href="#">Know More</a>
</section>

<section class="service art-left" style="top:960px">
  <div class="art" style="background:linear-gradient(135deg,#fbd3dc,#f4a7b9)" role="img" aria-label="Illustration of a pink piggy bank with a coin"></div>
  <div class="copy"><h3>Record Direct Bill Commission</h3><p>Lorem Ipsum is simply dummy text of the printing and typesetting industry. Lorem Ipsum has been the industry's standard dummy text ever since the 1500s, when an unknown printer took a galley of type and scrambled it to make a type specimen book.</p></div>
</section>

<section class="service tint art-right" style="top:1270px">
  <div class="copy"><h3>Reconcile &amp; Pay Agency Bill Premiums</h3><p>Lorem Ipsum is simply dummy text of the printing and typesetting industry. Lorem Ipsum has been the industry's standard dummy text ever since the 1500s, when an unknown printer took a galley of type and scrambled it to make a type specimen book.</p></div>
  <div class="art" style="background:linear-gradient(135deg,#c9e9b8,#4fb86a)" role="img" aria-label="Illustration of a hand holding a dollar bill"></div>
</section>

<section class="service art-left" style="top:1580px">
  <div class="art" style="background:linear-gradient(135deg,#f2f2f2,#d8dcdd)" role="img" aria-label="Illustration of a profit and loss statement"></div>
  <div class="copy"><h3>Reconcile General Ledger Accounts</h3><p>Lorem Ipsum is simply dummy text of the printing and typesetting industry. Lorem Ipsum has been the industry's standard dummy text ever since the 1500s, when an unknown printer took a galley of type and scrambled it to make a type specimen book.</p></div>
</section>

<section class="service tint art-right" style="top:1890px">
  <div class="copy"><h3>Prepare &amp; Interpret Financial Statements</h3><p>Lorem Ipsum is simply dummy text of the printing and typesetting industry. Lorem Ipsum has been the industry's standard dummy text ever since the 1500s, when an unknown printer took a galley of type and scrambled it to make a type specimen book.</p></div>
  <div class="art" style="background:linear-gradient(135deg,#f4f4f4,#e2e6e7)" role="img" aria-label="Illustration of a ruled document with a checkmark"></div>
</section>

<section class="service art-left" style="top:2200px">
  <div class="art" style="background:linear-gradient(135deg,#eef0f1,#d5dadc)" role="img" aria-label="Illustration of an invoice stamped paid"></div>
  <div class="copy"><h3>Pay Vendor Invoices</h3><p>Lorem Ipsum is simply dummy text of the printing and typesetting industry. Lorem Ipsum has been the industry's standard dummy text ever since the 1500s, when an unknown printer took a galley of type and scrambled it to make a type specimen book.</p></div>
</section>

<section class="service tint art-right" style="top:2510px">
  <div class="copy"><h3>Reconcile Customer Accounts Receivable</h3><p>Lorem Ipsum is simply dummy text of the printing and typesetting industry. Lorem Ipsum has been the industry's standard dummy text ever since the 1500s, when an unknown printer took a galley of type and scrambled it to make a type specimen book.</p></div>
  <div class="art" style="background:linear-gradient(135deg,#f7d6de,#e3456f)" role="img" aria-label="Illustration of a received stamp"></div>
</section>

<section class="service art-left" style="top:2820px">
  <div class="art" style="background:linear-gradient(135deg,#eef1f2,#cfd6d9)" role="img" aria-label="Illustration of an employee paycheck"></div>
  <div class="copy"><h3>Process Payroll</h3><p>Lorem Ipsum is simply dummy text of the printing and typesetting industry. Lorem Ipsum has been the industry's standard dummy text ever since the 1500s, when an unknown printer took a galley of type and scrambled it to make a type specimen book.</p></div>
</section>

<section class="why">
  <h2>Why it Works</h2>
  <div class="why-list">
    <div class="why-item">
      <svg viewBox="0 0 110 110" fill="none" stroke="#fff" stroke-width="4"><circle cx="55" cy="55" r="50"/><circle cx="55" cy="44" r="9" fill="#fff"/><path d="M38 72c2-10 9-14 17-14s15 4 17 14z" fill="#fff"/><circle cx="34" cy="50" r="6"/><circle cx="76" cy="50" r="6"/></svg>
      <span>Educated &amp; Trained Staff</span>
    </div>
    <div class="why-item">
      <svg viewBox="0 0 110 110" fill="none" stroke="#fff" stroke-width="4"><circle cx="55" cy="55" r="50"/><circle cx="55" cy="55" r="26"/><path d="M43 55l9 9 16-18"/></svg>
      <span>Quality Control</span>
    </div>
    <div class="why-item">
      <svg viewBox="0 0 110 110" fill="none" stroke="#fff" stroke-width="4"><circle cx="55" cy="55" r="50"/><path d="M30 45h44l-8-8M80 65H36l8 8"/></svg>
      <span>Separation of Duties</span>
    </div>
    <div class="why-item">
      <svg viewBox="0 0 110 110" fill="none" stroke="#fff" stroke-width="4"><circle cx="55" cy="55" r="50"/><rect x="38" y="50" width="34" height="26" rx="3" fill="#fff"/><path d="M44 50v-8a11 11 0 0 1 22 0v8"/></svg>
      <span>Data Security</span>
    </div>
  </div>
</section>

<footer class="site-footer">
  <div class="footer-bar">
    <div class="footer-links"><a class="pill" href="#">TERMS</a><a href="#">CONDITIONS</a><a href="#">DISCLAIMER</a><a href="#">FAQS</a></div>
    <div class="social"><i></i><i></i><i></i></div>
  </div>
  <div class="contact">
    <div><svg viewBox="0 0 24 24" fill="#fff"><path d="M12 2a7 7 0 0 0-7 7c0 5 7 13 7 13s7-8 7-13a7 7 0 0 0-7-7zm0 9.5A2.5 2.5 0 1 1 12 6.5a2.5 2.5 0 0 1 0 5z"/></svg>42 Quay Street, Harborview, CT 06000</div>
    <div><svg viewBox="0 0 24 24" fill="#fff"><path d="M6.6 10.8a15 15 0 0 0 6.6 6.6l2.2-2.2a1 1 0 0 1 1-.25 11 11 0 0 0 3.6.6 1 1 0 0 1 1 1V20a1 1 0 0 1-1 1A17 17 0 0 1 3 4a1 1 0 0 1 1-1h3.5a1 1 0 0 1 1 1 11 11 0 0 0 .6 3.6 1 1 0 0 1-.25 1z"/></svg>860-555-0142</div>
    <div><svg viewBox="0 0 24 24" fill="none" stroke="#fff" stroke-width="2"><rect x="3" y="5" width="18" height="14" rx="1"/><path d="M3 6l9 7 9-7"/></svg>info@harborlineledgerservices.com</div>
  </div>
  <div class="copyright">© Harborline Ledger &amp; Payroll Services · 2015. All Rights Reserved.</div>
</footer>

</body>
</html>
```